Harbor Washwell Laundry Service Company

I own a Coin Operated laundry business and need to include a picture of Coin operated machines.
Include:
Company Name: Harbor Washwell
For all your Coin Operated Laundry needs.Include: sales, service, and new installations with commissions as high as 50%
include 1873 N. 9th St, Arcadia, Ca 91006
626-318-7759
Include: Contact: Glen Moravec

Target Market(s)

coin Laundry

Industry/Entity Type

Business

Requirements
Must have
• picture of machines
• Sales, Service, Installations

```html
<!DOCTYPE html>
<html lang="en">
<head>
<meta charset="utf-8">
<title>Harbor Washwell Laundry Service Company – Postcard</title>
<link href="https://fonts.googleapis.com/css2?family=Arimo:wght@400;700&display=swap" rel="stylesheet">
<style>
  :root {
    --brand-blue: #2f7cc2;
    --brand-blue-deep: #2a72b8;
    --brand-blue-light: #5c9ad6;
    --ink: #2b2b2b;
    --swoosh-dark: #2a2c30;
    --paper: #ffffff;
    --backdrop: #e9e9e9;
    --rule: #9a9a9a;
    --machine-tone: #dcdfe3;
  }
  * { box-sizing: border-box; margin: 0; padding: 0; }
  html, body { width: 1200px; height: 1000px; overflow: hidden; }
  body {
    position: relative;
    background: var(--backdrop);
    font-family: "Arimo", Arial, sans-serif;
    color: var(--ink);
  }
  .postcard {
    position: absolute;
    background: var(--paper);
    overflow: hidden;
    box-shadow: 0 4px 14px rgba(0,0,0,0.25);
  }
  .postcard--front { left: 46px; top: 32px; width: 692px; height: 446px; }
  .postcard--back  { left: 441px; top: 509px; width: 692px; height: 448px; }
  .postcard__art { position: absolute; inset: 0; }
  .txt { position: absolute; white-space: nowrap; line-height: 1; }
  .lead { font-size: 24px; color: var(--ink); }
  .headline { font-size: 33px; font-weight: 700; color: var(--brand-blue); }
  .headline .soft { font-weight: 400; font-size: 24px; color: var(--ink); }
  .checklist { list-style: none; position: absolute; left: 38px; top: 178px; }
  .checklist li { position: relative; padding-left: 24px; font-size: 19px; line-height: 21px; margin-bottom: 11px; }
  .checklist svg { position: absolute; left: 0; top: 3px; }
  .checklist .highlight { color: var(--brand-blue); font-weight: 700; font-size: 18px; }
  .checklist .highlight b { font-size: 26px; }
  .address { font-size: 13px; color: var(--ink); }
  .phone { font-size: 21px; font-weight: 700; color: var(--brand-blue); display: flex; align-items: center; gap: 5px; }
  .machines {
    position: absolute;
    background: linear-gradient(180deg, #eef0f2 0%, var(--machine-tone) 60%, #c9cdd2 100%);
  }
  .contact-pill {
    position: absolute; left: 376px; top: 380px; width: 233px; height: 32px;
    background: #000; color: #fff; border-radius: 7px;
    font-size: 19px; font-weight: 700;
    display: flex; align-items: center; justify-content: center;
  }
  .back .lead { font-size: 21px; }
  .back .headline { font-size: 28px; }
  .back .headline .soft { font-size: 20px; }
  .callout { font-size: 14px; }
  .divider { position: absolute; left: 338px; top: 57px; width: 1px; height: 328px; background: #c8c8c8; }
  .mail-line { position: absolute; left: 408px; width: 208px; height: 1px; background: var(--rule); }
  .return-address { font-size: 13px; line-height: 16px; }
  .return-address strong { color: var(--brand-blue); }
</style>
</head>
<body>

<section class="postcard postcard--front" aria-label="Postcard front">
  <svg class="postcard__art" width="692" height="446" viewBox="0 0 692 446" aria-hidden="true">
    <path d="M430 0 C520 70 470 180 380 280 C330 340 300 400 284 446 L300 446 C330 380 380 320 430 260 C510 170 540 70 478 0 Z" fill="var(--swoosh-dark)"/>
    <path d="M478 0 L692 0 L692 446 L284 446 C310 380 360 310 420 250 C520 150 560 70 478 0 Z" fill="var(--brand-blue)"/>
    <path d="M600 0 C640 60 620 120 560 180 C630 130 680 80 692 40 L692 0 Z" fill="var(--brand-blue-light)" opacity="0.55"/>
    <path d="M692 250 C670 300 640 330 600 346 C650 340 680 320 692 300 Z" fill="var(--brand-blue-light)" opacity="0.5"/>
  </svg>

  <p class="txt lead" style="left:37px; top:55px;">For all your</p>
  <p class="txt headline" style="left:37px; top:86px;">Coin Operated</p>
  <p class="txt headline" style="left:37px; top:123px;">Laundry <span class="soft">needs</span></p>

  <ul class="checklist">
    <li><svg width="17" height="17" viewBox="0 0 17 17"><rect x="1" y="3" width="13" height="13" fill="none" stroke="var(--brand-blue-deep)" stroke-width="2"/><path d="M4 9 L8 13 L16 2" fill="none" stroke="var(--brand-blue-deep)" stroke-width="2.4"/></svg>Sales</li>
    <li><svg width="17" height="17" viewBox="0 0 17 17"><rect x="1" y="3" width="13" height="13" fill="none" stroke="var(--brand-blue-deep)" stroke-width="2"/><path d="M4 9 L8 13 L16 2" fill="none" stroke="var(--brand-blue-deep)" stroke-width="2.4"/></svg>Services</li>
    <li><svg width="17" height="17" viewBox="0 0 17 17"><rect x="1" y="3" width="13" height="13" fill="none" stroke="var(--brand-blue-deep)" stroke-width="2"/><path d="M4 9 L8 13 L16 2" fill="none" stroke="var(--brand-blue-deep)" stroke-width="2.4"/></svg>new installations<br>with commissions<br><span class="highlight">as high as <b>50%</b></span></li>
  </ul>

  <p class="txt address" style="left:37px; top:368px;">1873 N. 9th St, Arcadia, Ca 91006</p>
  <p class="txt phone" style="left:36px; top:385px;">
    <svg width="16" height="16" viewBox="0 0 16 16" aria-hidden="true"><circle cx="8" cy="8" r="7" fill="none" stroke="var(--ink)" stroke-width="1.4"/><path d="M5.5 4.5 L7 4.2 L7.6 6.2 L6.8 7 C7.3 8.2 8 8.9 9 9.3 L9.8 8.5 L11.6 9.1 L11.3 10.7 C8 11 5 8 5.5 4.5 Z" fill="var(--ink)"/></svg>
    626-318-7759
  </p>

  <div class="machines" role="img" aria-label="Photo of a white coin operated dryer and front-load washer side by side" style="left:319px; top:140px; width:330px; height:262px;"></div>
  <div class="contact-pill">Contact: Glen Moravec</div>
</section>

<section class="postcard postcard--back back" aria-label="Postcard back">
  <svg class="postcard__art" width="692" height="448" viewBox="0 0 692 448" aria-hidden="true">
    <path d="M0 295 C40 380 140 430 300 448 L270 448 C140 430 40 390 0 330 Z" fill="var(--swoosh-dark)"/>
    <path d="M0 330 C50 395 150 435 290 448 L0 448 Z" fill="var(--brand-blue)"/>
  </svg>

  <p class="txt lead" style="left:48px; top:40px;">For all your</p>
  <p class="txt headline" style="left:48px; top:67px;">Coin Operated</p>
  <p class="txt headline" style="left:48px; top:98px;">Laundry <span class="soft">needs</span></p>
  <p class="txt callout" style="left:48px; top:148px;">Call Us Today at</p>
  <p class="txt phone" style="left:47px; top:165px; font-size:22px;">
    <svg width="16" height="16" viewBox="0 0 16 16" aria-hidden="true"><circle cx="8" cy="8" r="7" fill="none" stroke="var(--ink)" stroke-width="1.4"/><path d="M5.5 4.5 L7 4.2 L7.6 6.2 L6.8 7 C7.3 8.2 8 8.9 9 9.3 L9.8 8.5 L11.6 9.1 L11.3 10.7 C8 11 5 8 5.5 4.5 Z" fill="var(--ink)"/></svg>
    626-318-7759
  </p>

  <div class="machines" role="img" aria-label="Photo of a white coin operated dryer and front-load washer side by side" style="left:39px; top:213px; width:230px; height:175px;"></div>

  <div class="divider"></div>
  <p class="txt return-address" style="left:368px; top:40px;">1873 N. 9th St, Arcadia,<br><strong>Ca 91006</strong></p>
  <div class="mail-line" style="top:199px;"></div>
  <div class="mail-line" style="top:255px;"></div>
  <div class="mail-line" style="top:311px;"></div>
</section>

</body>
</html>
```